Need Business Cards for my Business

email address: rkpmarlowhollowworks@vendrimail.com
web address: rkpmarlowhollowworks.net
Slogan: We offer various QVN licenses
Rowland K. Pemberly
Please stick with colors of Company Logo
would like the card to be more of the color example of the logo.
If you need PDF copy of logo email me at the above account.
Creative control rests with you.

Industry/Entity Type

Business

Contact Information for Business Card

I am a minimalist, but would like something to pop and stand out amongst other cards, make it memorable.

Font styles to use
Serif
Decorative
Script

```html
<!DOCTYPE html>
<html lang="en">
<head>
<meta charset="utf-8">
<title>RKP Marlow Hollow Works – Business Cards</title>
<link rel="stylesheet" href="https://fonts.googleapis.com/css2?family=Cinzel:wght@700&family=Great+Vibes&family=Lato:wght@300;400;700;900&display=swap">
<style>
  :root {
    --brand-red: #d4121f;
    --brand-red-dark: #b70f1a;
    --brand-blue: #1f5fa8;
    --ink: #2b2b2b;
    --ink-soft: #555a60;
    --ink-muted: #8a8e93;
    --paper: #fbfbfb;
    --stage: #e9e9ea;
    --rule-grey: #b9b9b9;
    --white: #ffffff;
  }
  * { box-sizing: border-box; margin: 0; padding: 0; }
  html, body {
    width: 800px; height: 1200px; overflow: hidden;
    background: var(--stage);
    font-family: "Lato", Arial, sans-serif;
  }
  .canvas { position: relative; width: 800px; height: 1200px; }
  .card {
    position: absolute; left: 80px; width: 640px; height: 366px;
    box-shadow: 0 14px 30px rgba(0,0,0,0.22);
    overflow: hidden;
  }

  /* Front */
  .card-front {
    top: 150px;
    background: linear-gradient(160deg, var(--brand-red) 0%, var(--brand-red-dark) 100%);
    color: var(--white);
  }
  .dotted-rule {
    position: absolute; left: 30px; right: 30px; height: 0;
    border-top: 2px dotted rgba(255,255,255,0.35);
  }
  .card-front .rule-top { top: 34px; }
  .card-front .rule-bottom-1 { bottom: 52px; }
  .card-front .rule-bottom-2 { bottom: 44px; }
  .card-front .rule-bottom-3 { bottom: 36px; }
  .front-brand {
    position: absolute; top: 118px; left: 0; right: 0;
    display: flex; align-items: center; justify-content: center; gap: 14px;
  }
  .brand-dot {
    width: 36px; height: 36px; border-radius: 50%;
    background: var(--white); flex: none;
  }
  .brand-name-front {
    font-family: "Cinzel", Georgia, serif;
    font-weight: 700; font-size: 26px; letter-spacing: 1px;
    color: var(--white); white-space: nowrap;
  }
  .front-slogan {
    position: absolute; top: 172px; left: 0; right: 0;
    text-align: center;
    font-family: "Great Vibes", cursive;
    font-size: 32px; color: rgba(255,255,255,0.92);
  }
  .front-web {
    position: absolute; right: 34px; bottom: 72px;
    font-size: 17px; letter-spacing: 0.5px; color: rgba(255,255,255,0.85);
  }

  /* Back */
  .card-back {
    top: 680px;
    background: var(--paper);
    color: var(--ink);
  }
  .card-back .rule-top { top: 40px; border-top: 2px dotted var(--rule-grey); }
  .back-brand {
    position: absolute; top: 68px; right: 34px;
    display: flex; align-items: center; gap: 12px;
  }
  .brand-square { width: 26px; height: 26px; background: var(--brand-blue); flex: none; }
  .brand-name-back {
    font-family: "Cinzel", Georgia, serif;
    font-weight: 700; font-size: 19px; letter-spacing: 0.5px;
    color: var(--brand-blue); white-space: nowrap;
  }
  .back-slogan {
    position: absolute; top: 102px; right: 34px;
    font-family: "Great Vibes", cursive;
    font-size: 24px; color: var(--brand-red);
  }
  .person { position: absolute; left: 34px; top: 152px; }
  .person-name {
    font-size: 27px; letter-spacing: 0.5px; text-transform: uppercase;
    font-weight: 300; color: var(--ink); line-height: 1.15;
  }
  .person-name strong { font-weight: 900; }
  .person-title {
    font-size: 19px; font-weight: 400; letter-spacing: 1px;
    text-transform: uppercase; color: var(--ink-soft); margin-top: 2px;
  }
  .red-rule {
    position: absolute; left: 34px; right: 34px; top: 232px;
    border-top: 2px dotted var(--brand-red);
  }
  .contacts {
    position: absolute; left: 34px; right: 34px; top: 246px;
    display: flex; gap: 26px; font-size: 15px; color: var(--ink);
  }
  .contact { display: flex; align-items: center; gap: 8px; white-space: nowrap; }
  .contact svg { flex: none; }
  .company { position: absolute; left: 34px; top: 290px; }
  .company-name {
    font-family: "Cinzel", Georgia, serif;
    font-weight: 700; font-size: 18px; letter-spacing: 0.5px;
    color: var(--ink-soft);
  }
  .company-address { font-size: 16px; color: var(--ink-muted); margin-top: 2px; }
  .card-back .rule-bottom {
    position: absolute; left: 34px; right: 34px; height: 0;
    border-top: 2px dotted rgba(212,18,31,0.45);
  }
  .card-back .rule-bottom-1 { bottom: 14px; }
  .card-back .rule-bottom-2 { bottom: 8px; }
</style>
</head>
<body>
<main class="canvas">

  <section class="card card-front" aria-label="Business card front">
    <div class="dotted-rule rule-top"></div>
    <div class="front-brand">
      <span class="brand-dot"></span>
      <span class="brand-name-front">RKP Marlow Hollow Works</span>
    </div>
    <p class="front-slogan">We offer various QVN licenses</p>
    <p class="front-web">www.rkpmarlowhollowworks.net</p>
    <div class="dotted-rule rule-bottom-1"></div>
    <div class="dotted-rule rule-bottom-2"></div>
    <div class="dotted-rule rule-bottom-3"></div>
  </section>

  <section class="card card-back" aria-label="Business card back">
    <div class="dotted-rule rule-top"></div>
    <div class="back-brand">
      <span class="brand-square"></span>
      <span class="brand-name-back">RKP Marlow Hollow Works</span>
    </div>
    <p class="back-slogan">We offer various QVN licenses</p>

    <div class="person">
      <h1 class="person-name"><strong>Rowland K.</strong> Pemberly</h1>
      <p class="person-title">Managing Director</p>
    </div>
    <div class="red-rule"></div>

    <div class="contacts">
      <span class="contact">
        <svg width="22" height="22" viewBox="0 0 22 22" aria-hidden="true">
          <rect x="0" y="0" width="22" height="22" rx="4" fill="#2b2b2b"/>
          <circle cx="11" cy="11" r="3" fill="none" stroke="#fff" stroke-width="1.6"/>
          <path d="M14 11v1.4a2 2 0 0 0 4 0V11a7 7 0 1 0-2.8 5.6" fill="none" stroke="#fff" stroke-width="1.6"/>
        </svg>
        rkpmarlowhollowworks@vendrimail.com
      </span>
      <span class="contact">
        <svg width="22" height="22" viewBox="0 0 22 22" aria-hidden="true">
          <rect x="0" y="0" width="22" height="22" rx="4" fill="#2b2b2b"/>
          <circle cx="11" cy="11" r="6.5" fill="none" stroke="#fff" stroke-width="1.3"/>
          <ellipse cx="11" cy="11" rx="2.8" ry="6.5" fill="none" stroke="#fff" stroke-width="1.2"/>
          <line x1="4.5" y1="11" x2="17.5" y2="11" stroke="#fff" stroke-width="1.2"/>
        </svg>
        rkpmarlowhollowworks.net
      </span>
    </div>

    <div class="company">
      <p class="company-name">RKP Marlow Hollow Works</p>
      <p class="company-address">West 18th Avenue, 9th Floor, Brookhaven, NY 11904</p>
    </div>
    <div class="rule-bottom rule-bottom-1"></div>
    <div class="rule-bottom rule-bottom-2"></div>
  </section>

</main>
</body>
</html>
```